" Window Blinds and Shutters Business Card Design"

We require a business card design for a new windows blinds and shutters company based in Sydney.
The business name is 'Larkvale Blinds and Shutters'.
We supply and install homes and businesses with internal and external window furnishings and finishes. This includes varieties of window blinds and window shutters.

Benefits of Larkvale Blinds and Shutters :
Added security and privacy,
The ability to control the amount of sunlight,
Regulate internal temperature.

Blinds varieties:
Roller Blinds, Double Roller Blinds, Roman Blinds, Vertical Blinds, Aluminium venetians, Timber venetians and PVC Venetians.

Shutters varieties:
Plantation Shutters, Aluminium Louvre Shutters, Roller Shutters and Security Shutters .
Updates

Hi Designers,

Please have a look at my Business card design brief. I need your help to start my new business.

Thanks,

Dorian.

Reason: not 100% happy with the options available, close to 90% happy, need a little more refinement. Thank You & Good Luck

Target Market(s)

Home owners, business owners, shift workers , and new home builders.

Industry/Entity Type

Security

Contact Information for Business Card

Larkvale Blinds and Shutters,

Dorian Kettlewell mobile: 0487561904,
Priya Hensworth mobile: 0472846015,

email: dorian.kettlewell@mailgrove.net
web: larkvaleblindsandshutters.com.au

Colors
ffffff
9d9d9d
f78f20

Requirements
Must have
• ON FRONT OF CARD
I have attached a picture of logo and need a designer to design a font logo for Larkvale Blinds and Shutters similar, or open to suggestions.

FRONT OF CARD
Company message/:
"Safeguarding windows by design"

BACK OF CARD
'For a FREE measure & quote call Dorian - 0487561904"
Nice to have
• Elegant yet professional.

Soft colours appealing to both male & female clients.

Should not have

• Unprofessional fonts

```html
<!DOCTYPE html>
<html lang="en">
<head>
<meta charset="utf-8">
<title>Larkvale Blinds and Shutters – Business Card</title>
<link rel="stylesheet" href="https://fonts.googleapis.com/css2?family=Quicksand:wght@500;700&display=swap">
<style>
  :root {
    --stage: #ebebeb;
    --card-white: #ffffff;
    --brand-grey: #8d8f92;
    --brand-orange: #f7971c;
    --ink-dark: #3a3a3a;
  }
  * { margin: 0; padding: 0; box-sizing: border-box; }
  html, body { width: 1200px; height: 1000px; overflow: hidden; }
  body {
    background: var(--stage);
    font-family: "Quicksand", sans-serif;
    position: relative;
  }
  .card {
    position: absolute;
    left: 110px;
    width: 700px;
    height: 400px;
    overflow: hidden;
    box-shadow: 0 6px 18px rgba(0,0,0,0.15);
  }

  /* Front */
  .card-front { top: 60px; background: var(--card-white); }
  .front-wordmark {
    position: absolute; top: 70px; left: 0; right: 0;
    text-align: center; color: var(--brand-grey); font-weight: 700;
  }
  .front-wordmark .name { font-size: 64px; letter-spacing: 4px; line-height: 1; text-transform: uppercase; }
  .front-wordmark .sub { font-size: 20px; letter-spacing: 6px; text-transform: uppercase; margin-top: 8px; }
  .front-tagline {
    position: absolute; top: 232px; left: 0; right: 0; text-align: center;
    color: var(--brand-grey); font-weight: 700; font-size: 22px;
    letter-spacing: 2px; text-transform: uppercase;
  }
  .front-band {
    position: absolute; left: 0; right: 0; bottom: 0; height: 96px;
    background: var(--brand-grey); color: var(--card-white);
    display: flex; align-items: center; justify-content: center;
    font-size: 21px; font-weight: 500; letter-spacing: 1px;
  }

  /* Back */
  .card-back { top: 500px; background: var(--brand-grey); color: var(--card-white); }
  .back-wordmark {
    position: absolute; top: 34px; right: 40px; text-align: right;
    color: var(--card-white); font-weight: 700; text-transform: uppercase;
  }
  .back-wordmark .name { font-size: 46px; line-height: 1; letter-spacing: 1px; }
  .back-wordmark .sub { font-size: 15px; letter-spacing: 3px; margin-top: 4px; }
  .contacts { position: absolute; right: 40px; top: 150px; text-align: right; }
  .people { display: flex; justify-content: flex-end; align-items: stretch; gap: 16px; }
  .person .name { font-weight: 700; font-size: 22px; }
  .person .phone { font-size: 19px; margin-top: 6px; display: flex; align-items: center; gap: 6px; }
  .person.primary .phone { justify-content: flex-end; }
  .person.secondary { text-align: left; }
  .divider { width: 1px; background: var(--card-white); }
  .line { font-size: 18px; margin-top: 12px; display: flex; align-items: center; justify-content: flex-end; gap: 8px; }
  .line.web { font-size: 21px; }
  .icon { width: 18px; height: 18px; flex: none; }
  .back-stripe { position: absolute; left: 0; bottom: 0; width: 700px; height: 40px; }

  /* Colour codes */
  .colour-codes { position: absolute; left: 960px; top: 790px; color: var(--ink-dark); }
  .colour-codes h2 { font-size: 20px; font-weight: 700; letter-spacing: 0.5px; margin-bottom: 16px; }
  .swatch-row { display: flex; align-items: center; gap: 14px; margin-bottom: 12px; font-size: 18px; font-weight: 500; }
  .swatch { width: 54px; height: 52px; }
  .swatch.grey { background: var(--brand-grey); }
  .swatch.orange { background: var(--brand-orange); }
</style>
</head>
<body>

<section class="card card-front">
  <div class="front-wordmark">
    <div class="name">Larkvale</div>
    <div class="sub">Blinds and Shutters</div>
  </div>
  <p class="front-tagline">Safeguarding windows by design</p>
  <div class="front-band">For a free measure and quote, call Dorian 0487561904</div>
</section>

<section class="card card-back">
  <div class="back-wordmark">
    <div class="name">Larkvale</div>
    <div class="sub">Blinds and Shutters</div>
  </div>

  <div class="contacts">
    <div class="people">
      <div class="person primary">
        <div class="name">Dorian Kettlewell</div>
        <div class="phone">0487561904
          <svg class="icon" viewBox="0 0 18 18"><rect x="5" y="2" width="8" height="14" rx="1.5" fill="none" stroke="var(--brand-orange)" stroke-width="1.5"/><line x1="8" y1="13.5" x2="10" y2="13.5" stroke="var(--brand-orange)" stroke-width="1.5"/></svg>
        </div>
      </div>
      <div class="divider"></div>
      <div class="person secondary">
        <div class="name">Priya Hensworth</div>
        <div class="phone">
          <svg class="icon" viewBox="0 0 18 18"><rect x="5" y="2" width="8" height="14" rx="1.5" fill="none" stroke="var(--brand-orange)" stroke-width="1.5"/><line x1="8" y1="13.5" x2="10" y2="13.5" stroke="var(--brand-orange)" stroke-width="1.5"/></svg>
          0472846015</div>
      </div>
    </div>
    <div class="line email">
      <svg class="icon" viewBox="0 0 18 18"><rect x="1.5" y="4" width="15" height="10" fill="none" stroke="var(--brand-orange)" stroke-width="1.5"/><polyline points="1.5,4 9,10 16.5,4" fill="none" stroke="var(--brand-orange)" stroke-width="1.5"/></svg>
      dorian.kettlewell@mailgrove.net
    </div>
    <div class="line web">
      <svg class="icon" viewBox="0 0 18 18"><circle cx="9" cy="9" r="7" fill="none" stroke="var(--brand-orange)" stroke-width="1.4"/><ellipse cx="9" cy="9" rx="3" ry="7" fill="none" stroke="var(--brand-orange)" stroke-width="1.2"/><line x1="2" y1="9" x2="16" y2="9" stroke="var(--brand-orange)" stroke-width="1.2"/></svg>
      www.larkvaleblindsandshutters.com.au
    </div>
  </div>

  <svg class="back-stripe" viewBox="0 0 700 40" preserveAspectRatio="none">
    <polygon points="0,26 490,26 490,40 0,40" fill="var(--card-white)"/>
    <polygon points="500,10 700,0 700,40 500,40" fill="var(--brand-orange)"/>
  </svg>
</section>

<aside class="colour-codes">
  <h2>COLOUR CODES</h2>
  <div class="swatch-row"><span class="swatch grey"></span># 8D8F92</div>
  <div class="swatch-row"><span class="swatch orange"></span># F7971C</div>
</aside>

</body>
</html>
```